Exercise Physiologist needs business cards

I have a logo, I need business cards (Sole trader) as I am moving to a new location and would like an updated look. I provide gym based exercise rehabilitation, injury prevention and movement assessments. I have over 13 years experience as an Exercise Physiologist. I would like the cards to look professional but not boring and can be a little different to stand out when sitting with other Allied Health Professional cards.

Target Market(s)

GP's, Allied health practitioners, people with injuries wanting to exercise

Industry/Entity Type

Health And Wellness

Contact Information for Business Card

Megan Dorrit - Exercise Physiologist 0437 582 906
14 Larkspur Bend Rd
Northbrook Vale
(Gate 5, Brannock Fitness)
vantorahealth@maildrop-example.com
socialpage-example.com/Vantora

Requirements
Must have
• I would like to include a section to add next appointment date and time space to the back of the card.
Nice to have
• Rounded corners and a black background on 1 or 2 sides.
Should not have
• Pictures of fit/toned bodies etc

```html
<!DOCTYPE html>
<html lang="en">
<head>
<meta charset="utf-8">
<title>Vantora Business Card – Megan Dorrit</title>
<link href="https://fonts.googleapis.com/css2?family=Arimo:ital,wght@0,400;0,700;1,400&family=Open+Sans:wght@600&display=swap" rel="stylesheet">
<style>
  :root {
    --backdrop: #dedede;
    --card: #f8f8f8;
    --ink: #4a4a4a;
    --brand-blue: #1a5bb8;
    --light-blue: #6fa6d8;
    --wash-blue: #dbe6f1;
    --box-line: #6d6d6d;
  }
  * { box-sizing: border-box; margin: 0; padding: 0; }
  html, body { width: 1200px; height: 960px; overflow: hidden; }
  body {
    background: var(--backdrop);
    font-family: "Arimo", Arial, sans-serif;
    color: var(--ink);
    position: relative;
  }
  .card {
    position: absolute;
    width: 600px;
    height: 343px;
    background: var(--card);
    overflow: hidden;
  }
  .card-front { left: 314px; top: 113px; }
  .card-back  { left: 311px; top: 472px; }

  /* front */
  .wash-ring { position: absolute; left: 312px; top: 22px; width: 310px; height: 310px; }
  .brand {
    position: absolute; left: 46px; top: 44px;
    display: flex; align-items: center; gap: 12px;
  }
  .brand-dot {
    width: 72px; height: 72px; border-radius: 50%;
    background: var(--brand-blue);
  }
  .brand-name {
    font-size: 40px; font-weight: 400; color: var(--brand-blue);
    letter-spacing: 0.5px;
  }
  .address {
    position: absolute; left: 46px; top: 181px;
    font-size: 14px; line-height: 18.5px; font-style: normal; color: #555;
  }
  .contact-list {
    position: absolute; left: 46px; top: 244px;
    list-style: none; font-size: 14px; color: #555;
  }
  .contact-list li { display: flex; align-items: center; gap: 8px; height: 19.5px; }
  .contact-list svg { width: 13px; height: 13px; flex: none; }
  .person {
    position: absolute; right: 47px; top: 219px; text-align: right;
  }
  .person-name {
    font-size: 20px; font-weight: 700; color: var(--brand-blue);
    letter-spacing: 0.3px;
  }
  .person-role {
    font-size: 15.5px; color: var(--light-blue); margin-top: 4px; letter-spacing: 0.3px;
  }
  .edge-tab {
    position: absolute; right: 0; top: 221px; width: 16px; height: 37px;
    background: var(--brand-blue);
  }

  /* back */
  .appt-title {
    position: absolute; top: 31px; width: 100%; text-align: center;
    font-family: "Open Sans", Arial, sans-serif; font-weight: 600;
    font-size: 21px; color: var(--brand-blue);
  }
  .row {
    position: absolute; left: 43px; right: 47px;
    display: flex; align-items: baseline;
  }
  .fill {
    border-bottom: 1.5px dotted #777; height: 1px;
  }
  .row-name { top: 92px; font-size: 16px; }
  .row-name .fill { flex: 1; margin: 0 4px 0 3px; }
  .row-when { top: 151px; color: var(--brand-blue); font-size: 17px; }
  .row-when .fill-date { flex: 0 0 227px; margin: 0 5px 0 14px; }
  .row-when .fill-time { flex: 1; margin: 0 8px 0 6px; }
  .ampm { font-size: 13px; }
  .days {
    position: absolute; left: 45px; top: 215px; width: 506px;
    display: flex; justify-content: space-between;
    list-style: none; color: var(--brand-blue); font-size: 16px;
  }
  .days li { display: flex; align-items: center; gap: 6px; }
  .days li::after {
    content: ""; width: 16px; height: 13px;
    border: 1.3px solid var(--box-line); border-radius: 2px; background: #fff;
  }
  .notice {
    position: absolute; top: 277px; width: 100%; text-align: center;
    font-style: italic; font-size: 13.5px; line-height: 17px; color: #555;
  }
</style>
</head>
<body>

<section class="card card-front">
  <svg class="wash-ring" viewBox="0 0 310 310" aria-hidden="true">
    <circle cx="155" cy="155" r="142" fill="none" stroke="var(--wash-blue)" stroke-width="18"/>
  </svg>

  <div class="brand">
    <span class="brand-dot"></span>
    <span class="brand-name">Vantora</span>
  </div>

  <address class="address">
    14 Larkspur Bend Rd<br>
    Northbrook Vale<br>
    (Gate 5, Brannock Fitness)
  </address>

  <ul class="contact-list">
    <li>
      <svg viewBox="0 0 16 16"><path fill="var(--brand-blue)" d="M3.6 1.2l2.3 2.6c.4.4.3 1-.1 1.4L4.6 6.4c.9 2 2.6 3.8 4.8 4.9l1.3-1.2c.4-.4 1-.4 1.4 0l2.5 2.2c.4.4.4 1 0 1.4l-1.3 1.3c-.7.7-1.8.9-2.7.4C6.3 13.3 2.9 9.9 1.1 5.6.7 4.7.9 3.7 1.6 3L2.3 1.2c.4-.4 1-.4 1.3 0z"/></svg>
      0437 582 906
    </li>
    <li>
      <svg viewBox="0 0 16 16"><rect x="1" y="3.5" width="14" height="9.5" rx="1" fill="var(--brand-blue)"/><path d="M1.5 4.2L8 9l6.5-4.8" fill="none" stroke="#fff" stroke-width="1.2"/></svg>
      name@vantorahealth-example.com
    </li>
    <li>
      <svg viewBox="0 0 16 16"><circle cx="8" cy="8" r="7" fill="var(--brand-blue)"/><path d="M1.5 8h13M8 1.2c-2.4 2-2.4 11.6 0 13.6M8 1.2c2.4 2 2.4 11.6 0 13.6" fill="none" stroke="#fff" stroke-width="1"/></svg>
      www.vantorahealth-example.com
    </li>
  </ul>

  <div class="person">
    <p class="person-name">MEGAN DORRIT</p>
    <p class="person-role">EXERCISE PHYSIOLOGIST</p>
  </div>
  <span class="edge-tab"></span>
</section>

<section class="card card-back">
  <h2 class="appt-title">Next Appointment</h2>

  <div class="row row-name">
    <span class="fill"></span>
    <span>has an appointment</span>
  </div>

  <div class="row row-when">
    <span>Date :</span>
    <span class="fill fill-date"></span>
    <span>Time :</span>
    <span class="fill fill-time"></span>
    <span class="ampm">AM/PM</span>
  </div>

  <ul class="days">
    <li>Sun</li><li>Mon</li><li>Tue</li><li>Wed</li><li>Thu</li><li>Fri</li><li>Sat</li>
  </ul>

  <p class="notice">
    Please give me 24 hours notice if you are unable to keep your appointment or<br>
    a cancellation fee may be charged.
  </p>
</section>

</body>
</html>
```